Etiketten für Kuchen im Glas
Zielgruppe
Die Firma Brelkat bietet kulinarische Präsente und Geschenkideen zum Thema kreatives Backen an. Unsere Zielgruppe ist B2C und Werbetreibende, die unsere Produkte als Geschenke einsetzen.
Aufgabenstellung
Für unsere Zielgruppe "Feinkostläden" benötigen wir ein etwas edleres klasssisches Etiketten-Design.
Gestaltet wird der Deckel und die Vorderseite eines Etiketts für ein 290 ml FUMS-Glas. Die entsprechende Designvorlage steht hier zum Download bereit:
https://files.tralvex-speicher.de/u/4827351/7902_01358_0000-Vorlage%20CMYK%20v08_2013-09.psd
Benötigt werden 4 unterschiedliche Etiketten, die aber aus einem "Guss" sein sollten für die Sorten: Stracciatella, Schokolade, Zitrone, Stollen. Die Sorte sollte mit auf dem Etikett stehen.
Sonstige Angaben auf dem Etikett:
- optional "Kuchen im Glas"
- gerne Grünhof Logo (siehe Anhang)
- optional "fertig gebacken". Könnte z.B. gut auf dem Deckel in Kombination mit "Kuchen im Gla" stehen
Achtung: Das Etikett für die Rückseite mit Deklaration muss nicht gestaltet werden.
Tipps: Das Etikett ist konisch und das Glas rund. Das bedeutet, dass Bilder + Schriften mit einer leichten Wölbung kreiert werden sollten. Für die Wölbung kann man sich gut an der unteren Designlinie orientieren.
Farbgestaltung: eher dunkel; z.B. Grau, Dunkelblau evtl. Schwarz
Schriften: Es dürfen auch kostenpflichtige Schriften verwendet werden. Freie Schriften allerdings bevorzugt
Format: Photoshop PSD inklusive allen Ebenen und verwendeten Elementen als einzelne Ebene.
Bei Fragen gerne melden, ich freue mich auf Eure Designs.

```html
<!DOCTYPE html>
<html lang="de">
<head>
<meta charset="utf-8">
<title>Kuchen im Glas – Etiketten</title>
<link rel="stylesheet" href="https://fonts.googleapis.com/css2?family=Pathway+Gothic+One&family=Allura&display=swap">
<style>
  :root {
    --paper: #ffffff;
    --label: #ebe3da;
    --flourish: #cdc1ae;
    --ink: #4a3f38;
    --zitrone: #f3a92a;
    --schokolade: #8a5636;
    --stracciatella: #6e6e6e;
    --stollen: #4d7a58;
  }
  * { margin: 0; padding: 0; box-sizing: border-box; }
  html, body { width: 886px; height: 1200px; overflow: hidden; background: var(--paper); }
  .sheet { position: relative; width: 886px; height: 1200px; }
  .label-set { position: absolute; left: 0; width: 886px; height: 260px; }
  .set-zitrone { top: 34px; --accent: var(--zitrone); }
  .set-schokolade { top: 315px; --accent: var(--schokolade); }
  .set-stracciatella { top: 602px; --accent: var(--stracciatella); }
  .set-stollen { top: 893px; --accent: var(--stollen); }
  .front-label { position: absolute; left: 60px; top: 0; width: 472px; height: 242px; }
  .lid-label { position: absolute; left: 601px; top: -2px; width: 224px; height: 224px; }
  .label-body { fill: var(--label); }
  .flourish-left { fill: url(#flourishLeft); }
  .flourish-right { fill: url(#flourishRight); }
  .flourish-lid { fill: url(#flourishLid); }
  .accent-ornament { fill: var(--accent); opacity: .4; }
  .rule-dark { stroke: var(--ink); stroke-width: 1; }
  .range-title { font-family: "Pathway Gothic One", "Arial Narrow", sans-serif; font-size: 29px; fill: var(--ink); letter-spacing: .3px; }
  .flavour-name { font-family: "Allura", cursive; fill: var(--accent); stroke: #fbf8f3; stroke-width: 4px; paint-order: stroke; }
  .lid-title { font-family: "Pathway Gothic One", "Arial Narrow", sans-serif; font-size: 33px; fill: var(--ink); letter-spacing: .3px; }
</style>
</head>
<body>
<svg width="0" height="0" style="position:absolute" aria-hidden="true">
  <defs>
    <clipPath id="frontShape" clipPathUnits="userSpaceOnUse">
      <path d="M6,20 Q236,-6 466,20 Q472,22 471,28 L442,232 Q440,238 432,238 Q236,222 40,238 Q32,238 30,232 L1,28 Q0,22 6,20 Z"/>
    </clipPath>
    <clipPath id="lidShape" clipPathUnits="userSpaceOnUse">
      <circle cx="112" cy="112" r="112"/>
    </clipPath>
    <linearGradient id="flourishLeft" x1="0" y1="0" x2="1" y2="0">
      <stop offset="0%" stop-color="#cdc1ae" stop-opacity=".75"/>
      <stop offset="100%" stop-color="#cdc1ae" stop-opacity="0"/>
    </linearGradient>
    <linearGradient id="flourishRight" x1="1" y1="0" x2="0" y2="0">
      <stop offset="0%" stop-color="#cdc1ae" stop-opacity=".75"/>
      <stop offset="100%" stop-color="#cdc1ae" stop-opacity="0"/>
    </linearGradient>
    <linearGradient id="flourishLid" x1="1" y1="0" x2="0" y2="1">
      <stop offset="0%" stop-color="#d6cbbb" stop-opacity=".7"/>
      <stop offset="100%" stop-color="#d6cbbb" stop-opacity=".15"/>
    </linearGradient>
  </defs>
</svg>

<main class="sheet">

  <section class="label-set set-zitrone">
    <svg class="front-label" viewBox="0 0 472 242">
      <g clip-path="url(#frontShape)">
        <rect class="label-body" width="472" height="242"/>
        <rect class="flourish-left" role="img" aria-label="Rankenornament links" x="0" y="0" width="170" height="242"/>
        <rect class="flourish-right" role="img" aria-label="Rankenornament rechts" x="302" y="0" width="170" height="242"/>
      </g>
      <rect class="accent-ornament" role="img" aria-label="Zierornament über dem Titel" x="176" y="22" width="120" height="22" rx="11"/>
      <line class="rule-dark" x1="166" y1="50" x2="306" y2="50"/>
      <text class="range-title" x="236" y="78" text-anchor="middle">KUCHEN IM GLAS</text>
      <line class="rule-dark" x1="166" y1="85" x2="306" y2="85"/>
      <rect class="accent-ornament" role="img" aria-label="Zierornament unter dem Titel" x="206" y="89" width="60" height="12" rx="6"/>
      <text class="flavour-name" x="236" y="178" text-anchor="middle" font-size="80">Zitrone</text>
    </svg>
    <svg class="lid-label" viewBox="0 0 224 224">
      <g clip-path="url(#lidShape)">
        <rect class="label-body" width="224" height="224"/>
        <rect class="flourish-lid" role="img" aria-label="Rankenornament im Hintergrund" width="224" height="224"/>
      </g>
      <rect class="accent-ornament" role="img" aria-label="Zierornament über dem Schriftzug" x="40" y="62" width="144" height="40" rx="14"/>
      <line class="rule-dark" x1="24" y1="108" x2="200" y2="108"/>
      <text class="lid-title" x="112" y="140" text-anchor="middle">FERTIG GEBACKEN</text>
      <line class="rule-dark" x1="24" y1="148" x2="200" y2="148"/>
      <rect class="accent-ornament" role="img" aria-label="Zierornament unter dem Schriftzug" x="62" y="152" width="100" height="20" rx="8"/>
    </svg>
  </section>

  <section class="label-set set-schokolade">
    <svg class="front-label" viewBox="0 0 472 242">
      <g clip-path="url(#frontShape)">
        <rect class="label-body" width="472" height="242"/>
        <rect class="flourish-left" role="img" aria-label="Rankenornament links" x="0" y="0" width="170" height="242"/>
        <rect class="flourish-right" role="img" aria-label="Rankenornament rechts" x="302" y="0" width="170" height="242"/>
      </g>
      <rect class="accent-ornament" role="img" aria-label="Zierornament über dem Titel" x="176" y="22" width="120" height="22" rx="11"/>
      <line class="rule-dark" x1="166" y1="50" x2="306" y2="50"/>
      <text class="range-title" x="236" y="78" text-anchor="middle">KUCHEN IM GLAS</text>
      <line class="rule-dark" x1="166" y1="85" x2="306" y2="85"/>
      <rect class="accent-ornament" role="img" aria-label="Zierornament unter dem Titel" x="206" y="89" width="60" height="12" rx="6"/>
      <text class="flavour-name" x="236" y="178" text-anchor="middle" font-size="66">Schokolade</text>
    </svg>
    <svg class="lid-label" viewBox="0 0 224 224">
      <g clip-path="url(#lidShape)">
        <rect class="label-body" width="224" height="224"/>
        <rect class="flourish-lid" role="img" aria-label="Rankenornament im Hintergrund" width="224" height="224"/>
      </g>
      <rect class="accent-ornament" role="img" aria-label="Zierornament über dem Schriftzug" x="40" y="62" width="144" height="40" rx="14"/>
      <line class="rule-dark" x1="24" y1="108" x2="200" y2="108"/>
      <text class="lid-title" x="112" y="140" text-anchor="middle">FERTIG GEBACKEN</text>
      <line class="rule-dark" x1="24" y1="148" x2="200" y2="148"/>
      <rect class="accent-ornament" role="img" aria-label="Zierornament unter dem Schriftzug" x="62" y="152" width="100" height="20" rx="8"/>
    </svg>
  </section>

  <section class="label-set set-stracciatella">
    <svg class="front-label" viewBox="0 0 472 242">
      <g clip-path="url(#frontShape)">
        <rect class="label-body" width="472" height="242"/>
        <rect class="flourish-left" role="img" aria-label="Rankenornament links" x="0" y="0" width="170" height="242"/>
        <rect class="flourish-right" role="img" aria-label="Rankenornament rechts" x="302" y="0" width="170" height="242"/>
      </g>
      <rect class="accent-ornament" role="img" aria-label="Zierornament über dem Titel" x="176" y="22" width="120" height="22" rx="11"/>
      <line class="rule-dark" x1="166" y1="50" x2="306" y2="50"/>
      <text class="range-title" x="236" y="78" text-anchor="middle">KUCHEN IM GLAS</text>
      <line class="rule-dark" x1="166" y1="85" x2="306" y2="85"/>
      <rect class="accent-ornament" role="img" aria-label="Zierornament unter dem Titel" x="206" y="89" width="60" height="12" rx="6"/>
      <text class="flavour-name" x="236" y="184" text-anchor="middle" font-size="68">Stracciatella</text>
    </svg>
    <svg class="lid-label" viewBox="0 0 224 224">
      <g clip-path="url(#lidShape)">
        <rect class="label-body" width="224" height="224"/>
        <rect class="flourish-lid" role="img" aria-label="Rankenornament im Hintergrund" width="224" height="224"/>
      </g>
      <rect class="accent-ornament" role="img" aria-label="Zierornament über dem Schriftzug" x="40" y="62" width="144" height="40" rx="14"/>
      <line class="rule-dark" x1="24" y1="108" x2="200" y2="108"/>
      <text class="lid-title" x="112" y="140" text-anchor="middle">FERTIG GEBACKEN</text>
      <line class="rule-dark" x1="24" y1="148" x2="200" y2="148"/>
      <rect class="accent-ornament" role="img" aria-label="Zierornament unter dem Schriftzug" x="62" y="152" width="100" height="20" rx="8"/>
    </svg>
  </section>

  <section class="label-set set-stollen">
    <svg class="front-label" viewBox="0 0 472 242">
      <g clip-path="url(#frontShape)">
        <rect class="label-body" width="472" height="242"/>
        <rect class="flourish-left" role="img" aria-label="Rankenornament links" x="0" y="0" width="170" height="242"/>
        <rect class="flourish-right" role="img" aria-label="Rankenornament rechts" x="302" y="0" width="170" height="242"/>
      </g>
      <rect class="accent-ornament" role="img" aria-label="Zierornament über dem Titel" x="176" y="22" width="120" height="22" rx="11"/>
      <line class="rule-dark" x1="166" y1="50" x2="306" y2="50"/>
      <text class="range-title" x="236" y="78" text-anchor="middle">KUCHEN IM GLAS</text>
      <line class="rule-dark" x1="166" y1="85" x2="306" y2="85"/>
      <rect class="accent-ornament" role="img" aria-label="Zierornament unter dem Titel" x="206" y="89" width="60" height="12" rx="6"/>
      <text class="flavour-name" x="236" y="188" text-anchor="middle" font-size="90">Stollen</text>
    </svg>
    <svg class="lid-label" viewBox="0 0 224 224">
      <g clip-path="url(#lidShape)">
        <rect class="label-body" width="224" height="224"/>
        <rect class="flourish-lid" role="img" aria-label="Rankenornament im Hintergrund" width="224" height="224"/>
      </g>
      <rect class="accent-ornament" role="img" aria-label="Zierornament über dem Schriftzug" x="40" y="62" width="144" height="40" rx="14"/>
      <line class="rule-dark" x1="24" y1="108" x2="200" y2="108"/>
      <text class="lid-title" x="112" y="140" text-anchor="middle">FERTIG GEBACKEN</text>
      <line class="rule-dark" x1="24" y1="148" x2="200" y2="148"/>
      <rect class="accent-ornament" role="img" aria-label="Zierornament unter dem Schriftzug" x="62" y="152" width="100" height="20" rx="8"/>
    </svg>
  </section>

</main>
</body>
</html>
```